Business broker needs designs for business card, letterhead and email signature

I require the following items:
- business cards
- letterhead
- email signature

My company is a Business Broker company that specialises in business sales across various industries. The company has branches in four areas and each area has its own logo and website. Initially for the submission I am happy to inspect 1 design and 1 layout for tallowgatedeals but the winner will need to complete a design for each area.

The four areas are:
1. tallowgatedeals
2. pinecrestfuelagent
3. harrowlinkagent
4. bramblegroceragent

I would like one design for each of the above items for each area. In each design, there should be one prominent logo and then the remaining three should also be included, for eg, the letterhead for the tallowgatedeal area would have the tallowgatedeal logo featuring prominently, somewhere at the top perhaps and the logos of the other three areas would be smaller and perhaps at the bottom, down the side, etc.

For the business cards, one prominent logo should feature on one side with the remaining three logos on the reverse.

The overall objective is for each item to look like it belongs to one family . I need all the source files as I may add new industries moving forward.

Target Market(s)

My company targets business minded people looking to increase wealth,. make an investment or migrate to Australia. People who busy and are looking for efficient and professional service in securing their next business venture.

Industry/Entity Type

Business

Font styles to use
Serif
Sans Serif

Requirements
Must have
• I want something professional and corporate looking, not something cartoony or playful. I am happy for you to be creative.

```html
<!DOCTYPE html>
<html lang="en">
<head>
<meta charset="utf-8">
<title>Tallowgatedeals business card</title>
<link rel="stylesheet" href="https://fonts.googleapis.com/css2?family=Roboto+Condensed:wght@700&family=Questrial&display=swap">
<style>
  :root {
    --bg: #e4e3e8;
    --slate: #34444f;
    --slate-line: #4d5d68;
    --red: #d0112b;
    --teal: #1bb3b0;
    --amber: #f2a900;
    --green: #1fae3a;
    --paper: #f6f7f9;
    --ghost: #e3e7eb;
    --ink: #34444f;
    --white: #ffffff;
  }
  * { box-sizing: border-box; margin: 0; padding: 0; }
  html, body { width: 1200px; height: 934px; overflow: hidden; }
  body {
    background: var(--bg);
    font-family: "Questrial", sans-serif;
    position: relative;
  }
  .card {
    position: absolute;
    top: 302px;
    width: 540px;
    height: 330px;
    overflow: hidden;
    box-shadow: 0 6px 18px rgba(40, 50, 60, 0.18);
  }

  /* Reverse side */
  .card-back { left: 40px; background: var(--slate); }
  .divider { position: absolute; background: var(--slate-line); }
  .divider-h { left: 30px; right: 30px; top: 165px; height: 1px; }
  .divider-v { top: 25px; bottom: 25px; left: 270px; width: 1px; }
  .centre-dot {
    position: absolute; left: 246px; top: 141px;
    width: 48px; height: 48px; border-radius: 50%;
    background: #4a5a65;
  }
  .area-name {
    position: absolute;
    display: flex; align-items: center; gap: 8px;
    font-family: "Roboto Condensed", sans-serif;
    font-weight: 700; font-size: 19px; letter-spacing: -0.2px;
    width: 270px; justify-content: center;
  }
  .area-name .dot {
    width: 16px; height: 16px; border-radius: 50%; background: var(--white);
  }
  .area-tl { left: 0; top: 70px; color: var(--red); }
  .area-tr { left: 270px; top: 70px; color: var(--teal); }
  .area-bl { left: 0; top: 240px; color: var(--amber); }
  .area-br { left: 270px; top: 240px; color: var(--green); }

  /* Front side */
  .card-front { left: 620px; background: var(--paper); }
  .band-red { position: absolute; left: 0; top: 0; width: 310px; height: 12px; background: var(--red); }
  .band-slate { position: absolute; left: 310px; right: 0; top: 0; height: 7px; background: var(--slate); }
  .ghost-circle {
    position: absolute; right: -20px; top: -40px;
    width: 210px; height: 210px; border-radius: 50%;
    background: var(--ghost);
  }
  .brand {
    position: absolute; left: 36px; top: 82px;
    display: flex; align-items: center; gap: 10px;
    font-family: "Roboto Condensed", sans-serif;
    font-weight: 700; font-size: 34px; letter-spacing: -0.6px;
    color: var(--ink);
  }
  .brand .dot { width: 34px; height: 34px; border-radius: 50%; background: var(--ink); }
  .person { position: absolute; left: 36px; top: 180px; }
  .person-name { color: var(--red); font-size: 17px; letter-spacing: 0.5px; text-transform: uppercase; font-weight: 700; }
  .person-role { color: var(--ink); font-size: 13px; margin-top: 2px; }
  .contacts { position: absolute; left: 36px; top: 248px; list-style: none; }
  .contacts li {
    display: flex; align-items: center; gap: 9px;
    font-size: 13px; color: var(--ink); height: 20px;
  }
  .icon { width: 15px; height: 15px; border-radius: 3px; background: var(--red); display: block; }
  .address {
    position: absolute; right: 36px; top: 170px;
    text-align: right; font-size: 13px; line-height: 1.45; color: var(--ink);
  }
</style>
</head>
<body>

<section class="card card-back" aria-label="Card reverse">
  <div class="divider divider-h"></div>
  <div class="divider divider-v"></div>
  <div class="centre-dot"></div>
  <div class="area-name area-tl"><span class="dot"></span>tallowgatedeals</div>
  <div class="area-name area-tr"><span class="dot"></span>pinecrestfuelagent</div>
  <div class="area-name area-bl"><span class="dot"></span>harrowlinkagent</div>
  <div class="area-name area-br"><span class="dot"></span>bramblegroceragent</div>
</section>

<section class="card card-front" aria-label="Card front">
  <div class="band-red"></div>
  <div class="band-slate"></div>
  <div class="ghost-circle"></div>

  <div class="brand"><span class="dot"></span>tallowgatedeals</div>

  <div class="person">
    <p class="person-name">Morgan Ellery</p>
    <p class="person-role">Director</p>
  </div>

  <ul class="contacts">
    <li>
      <svg class="icon" viewBox="0 0 15 15"><rect width="15" height="15" rx="3" fill="#d0112b"/><path d="M4.5 3.5c.6-.3 1.2 0 1.4.5l.5 1.3c.1.4 0 .7-.3.9l-.6.4c.5 1 1.3 1.8 2.3 2.3l.4-.6c.2-.3.6-.4.9-.3l1.3.5c.5.2.8.8.5 1.4-.4.8-1.3 1.2-2.1.9C6.7 10 5 8.3 4.2 6.2c-.3-.9.1-2.3.3-2.7z" fill="#fff"/></svg>
      1300 555 218
    </li>
    <li>
      <svg class="icon" viewBox="0 0 15 15"><rect width="15" height="15" rx="3" fill="#d0112b"/><rect x="3" y="4.5" width="9" height="6" fill="none" stroke="#fff" stroke-width="1"/><path d="M3 4.5l4.5 3.5 4.5-3.5" fill="none" stroke="#fff" stroke-width="1"/></svg>
      info@tallowgatedeals.com.au
    </li>
    <li>
      <svg class="icon" viewBox="0 0 15 15"><rect width="15" height="15" rx="3" fill="#d0112b"/><circle cx="7.5" cy="7.5" r="4" fill="none" stroke="#fff" stroke-width="1"/><path d="M3.5 7.5h8M7.5 3.5c-1.6 2.2-1.6 5.8 0 8M7.5 3.5c1.6 2.2 1.6 5.8 0 8" fill="none" stroke="#fff" stroke-width="0.8"/></svg>
      www.tallowgatedeals.com.au
    </li>
  </ul>

  <address class="address" style="font-style: normal;">
    Level 12, Harbour House<br>
    88 Kent Lane<br>
    Sydney NSW 2000
  </address>
</section>

</body>
</html>
```